Apartment Investor Business Card Design

Need a new business card designed for my multifamily investment company

Industry/Entity Type

Real Estate

Contact Information for Business Card

Marlow Pickett - President & CEO
Brightfield Capital, LLC
4870 North 52nd Avenue, Ste 150
Omaha, NE 68231
(402) 555-0193
Marlow@brightfieldcapitalmidwest.example
Www.BrightfieldCapitalMidwest.example

Colors
3176b5

```html
<!DOCTYPE html>
<html lang="en">
<head>
<meta charset="utf-8">
<title>Brightfield Capital – Business Card</title>
<link rel="stylesheet" href="https://fonts.googleapis.com/css2?family=Cinzel:wght@400&family=EB+Garamond:wght@400;600;700&display=swap">
<style>
  :root {
    --page-bg: #ececec;
    --card-dark: #2b2b2b;
    --card-light: #f5f5f5;
    --brand-blue: #3176b5;
    --text-white: #ffffff;
    --text-dark: #1e1e1e;
    --text-grey: #7a7a7a;
    --band-grey: #8c8c8c;
  }
  * { margin: 0; padding: 0; box-sizing: border-box; }
  html, body {
    width: 1200px;
    height: 757px;
    overflow: hidden;
    background: var(--page-bg);
  }
  .canvas {
    position: relative;
    width: 1200px;
    height: 757px;
  }
  .card {
    position: absolute;
    top: 195px;
    width: 498px;
    height: 298px;
    overflow: hidden;
  }
  .card--front { left: 85px; background: var(--card-dark); }
  .card--back  { left: 650px; background: var(--card-light); }

  .brand-square {
    position: absolute;
    left: 50%;
    background: var(--brand-blue);
    transform: translateX(-50%);
  }
  .brand-name {
    position: absolute;
    left: 0;
    width: 100%;
    text-align: center;
    font-family: "Cinzel", serif;
    font-weight: 400;
    white-space: nowrap;
  }
  .card--front .brand-square { top: 92px; width: 46px; height: 46px; }
  .card--front .brand-name {
    top: 164px;
    font-size: 30px;
    letter-spacing: 0.5px;
    color: var(--text-white);
  }
  .website {
    position: absolute;
    top: 268px;
    left: 0;
    width: 100%;
    text-align: center;
    font-family: "EB Garamond", serif;
    font-weight: 700;
    font-size: 11px;
    letter-spacing: 1.6px;
    color: var(--text-white);
  }
  .website__domain { color: var(--brand-blue); }

  .card--back .brand-square { top: 50px; width: 30px; height: 30px; }
  .card--back .brand-name {
    top: 96px;
    font-size: 20px;
    color: var(--text-dark);
  }
  .person {
    position: absolute;
    left: 33px;
    top: 168px;
    font-family: "EB Garamond", serif;
  }
  .person__name {
    font-weight: 700;
    font-size: 13px;
    color: var(--brand-blue);
    line-height: 16px;
  }
  .person__title {
    font-size: 10px;
    color: var(--text-dark);
    line-height: 13px;
  }
  .contact {
    position: absolute;
    left: 33px;
    top: 228px;
    font-family: "EB Garamond", serif;
    font-size: 11px;
    color: var(--text-dark);
    list-style: none;
  }
  .contact__item {
    display: flex;
    align-items: center;
    gap: 6px;
    height: 19px;
  }
  .contact__icon { width: 10px; height: 10px; fill: var(--brand-blue); }
  .company {
    position: absolute;
    right: 22px;
    top: 228px;
    text-align: right;
    font-family: "EB Garamond", serif;
  }
  .company__name {
    font-weight: 700;
    font-size: 13px;
    letter-spacing: 0.3px;
    color: var(--brand-blue);
    line-height: 19px;
  }
  .company__address {
    font-weight: 600;
    font-size: 10.5px;
    color: var(--text-grey);
    line-height: 19px;
  }
  .card__band {
    position: absolute;
    left: 0;
    bottom: 0;
    width: 100%;
    height: 11px;
    background: var(--band-grey);
  }
</style>
</head>
<body>
<main class="canvas">

  <section class="card card--front" aria-label="Card front">
    <div class="brand-square"></div>
    <div class="brand-name">BRIGHTFIELD CAPITAL</div>
    <div class="website">www.<span class="website__domain">BrightfieldCapitalMidwest</span>.example</div>
  </section>

  <section class="card card--back" aria-label="Card back">
    <div class="brand-square"></div>
    <div class="brand-name">BRIGHTFIELD CAPITAL</div>

    <div class="person">
      <div class="person__name">Marlow Pickett</div>
      <div class="person__title">President &amp; CEO</div>
    </div>

    <ul class="contact">
      <li class="contact__item">
        <svg class="contact__icon" viewBox="0 0 10 10" aria-hidden="true">
          <path d="M1 3.5 C1 2 3 1 5 1 C7 1 9 2 9 3.5 L7 4 L6.6 3 L3.4 3 L3 4 Z"/>
          <rect x="2.2" y="4.5" width="5.6" height="4.5" rx="0.8"/>
        </svg>
        (402) 555-0193
      </li>
      <li class="contact__item">
        <svg class="contact__icon" viewBox="0 0 10 10" aria-hidden="true">
          <path d="M0.5 2 H9.5 V8.5 H0.5 Z M1.2 2.6 L5 5.6 L8.8 2.6" stroke="#f5f5f5" stroke-width="0.7"/>
        </svg>
        Marlow@brightfieldcapitalmidwest.example
      </li>
    </ul>

    <div class="company">
      <div class="company__name">BRIGHTFIELD CAPITAL, LLC</div>
      <div class="company__address">4870 North 52nd Avenue, Ste 150 Omaha, NE 68231</div>
    </div>

    <div class="card__band"></div>
  </section>

</main>
</body>
</html>
```